Flyer Design Project

We are a storm restoration company that has recently begun restoration from water/flood damage from Hurricane Sandy. We provide disaster relief to homeowners and or commercial property owners after a flood. To start we offer cleanup and remediation which is taking out and disposing of all wet items in a home or business and the cutting out of walls, flooring and other items affected by a flood. We then provide remediation which includes the drying out of a home or business along with a dehumidifier to take all the moisture out of the air and to put it simply dry out the home. We also uses chemicals to clean and provide mold remediation to prevent to growth of mold. We work directly with a customers insurance company if they have flood insurance and after that we provide the services to rebuild and bring their property back to its condition before the storm.

Im looking for an informational type flier that I could insert into our business folders that we give to customers and also to use as fliers to pass out to potential customers. I want potential customers to look at this and feel comfortable with calling my company and working with us.

Company name Brellwick Building Partners. I attached our company logo.

Target Market(s)

Those affected by flooding from Hurricane Sandy

Industry/Entity Type

Insurance

Requirements
Must have
• Company logo, name and colors on flier
Nice to have
• Color photos that have to do with water restoration or showing flood damamge

```html
<!DOCTYPE html>
<html lang="en">
<head>
<meta charset="utf-8">
<title>Storm Restoration – Brellwick Building Partners</title>
<link href="https://fonts.googleapis.com/css2?family=Nunito:wght@800;900&family=Open+Sans:wght@400;600;700&display=swap" rel="stylesheet">
<style>
  :root {
    --blue: #0f7cc4;
    --blue-deep: #0a5d9c;
    --blue-light: #2fa2e3;
    --yellow: #f3e21b;
    --mint: #9fe3d6;
    --ink: #2a2a2a;
    --heading-blue: #1580c8;
    --panel-grey: #e6e7e9;
    --page: #ffffff;
  }
  * { box-sizing: border-box; margin: 0; padding: 0; }
  html, body { width: 1200px; height: 872px; overflow: hidden; background: var(--page); }
  .flyer {
    position: relative; width: 1200px; height: 872px; overflow: hidden;
    background: linear-gradient(180deg, #ffffff 0%, #f4f5f6 60%, #e9eaec 100%);
    font-family: "Open Sans", Arial, sans-serif; color: var(--ink);
  }
  .hero-photo {
    position: absolute; left: 0; top: 0; width: 600px; height: 660px;
    background: linear-gradient(180deg, #c9ccd0 0%, #e8e8e6 30%, #f2f2ef 48%, #8f8a78 62%, #6f6a58 80%, #5c5848 100%);
    clip-path: polygon(0 0, 540px 0, 490px 360px, 420px 660px, 0 660px);
  }
  .blue-band {
    position: absolute; left: 0; top: 0; width: 1200px; height: 360px;
    background: linear-gradient(180deg, var(--blue-light) 0%, var(--blue) 30%, var(--blue-deep) 100%);
    clip-path: polygon(560px 0, 1200px 0, 1200px 360px, 510px 360px);
  }
  .title {
    position: absolute; left: 700px; top: 28px; width: 420px; text-align: center;
    font-family: "Nunito", Arial, sans-serif; font-weight: 900; line-height: 1;
  }
  .title .storm { display: block; font-size: 48px; color: var(--yellow); }
  .title .restoration {
    display: block; font-size: 52px; margin-top: 2px;
    background: linear-gradient(180deg, #e4fff8 0%, var(--mint) 55%, #5cc7c0 100%);
    -webkit-background-clip: text; background-clip: text; color: transparent;
  }
  .brand {
    position: absolute; left: 545px; top: 178px; width: 300px;
    display: flex; flex-direction: column; align-items: center; gap: 10px;
    font-family: "Nunito", Arial, sans-serif; font-weight: 900; color: #ffffff;
    font-size: 25px; line-height: 1.1; text-align: center;
  }
  .brand-dot { width: 46px; height: 46px; border-radius: 50%; background: var(--yellow); }
  .intro {
    position: absolute; left: 878px; top: 178px; width: 300px;
    color: #ffffff; font-weight: 700; font-size: 21px; line-height: 29px;
  }
  .inset { position: absolute; background: #ffffff; padding: 5px; }
  .inset .fill { width: 100%; height: 100%; }
  .inset-fan { left: 478px; top: 378px; width: 240px; height: 130px;
    clip-path: polygon(22px 0, 100% 0, calc(100% - 22px) 100%, 0 100%); }
  .inset-fan .fill { background: linear-gradient(135deg, #8a7a66 0%, #3a77a8 45%, #2b5f86 70%, #6d6558 100%); }
  .inset-policy { left: 410px; top: 522px; width: 285px; height: 130px;
    clip-path: polygon(24px 0, 100% 0, calc(100% - 24px) 100%, 0 100%); }
  .inset-policy .fill { background: linear-gradient(160deg, #f4f2ec 0%, #dcd9d0 60%, #a9a59a 100%); }
  .service { position: absolute; left: 764px; top: 366px; width: 410px; }
  .service h2 {
    font-family: "Nunito", Arial, sans-serif; font-weight: 900; font-size: 26px;
    color: var(--heading-blue); margin-left: 30px; margin-bottom: 6px;
  }
  .service p { font-size: 16.4px; line-height: 24px; }
  .footer-strip {
    position: absolute; left: 0; top: 662px; width: 1200px; height: 210px;
    background: linear-gradient(180deg, #eeeff0 0%, #dcdde0 100%);
  }
  .contact {
    position: absolute; left: 70px; top: 676px; width: 590px; height: 144px;
    background: linear-gradient(135deg, var(--blue-light) 0%, var(--blue) 60%, var(--blue-deep) 100%);
    clip-path: polygon(0 0, 100% 0, calc(100% - 20px) 100%, 0 100%);
    color: #ffffff; font-weight: 700; font-size: 17px; line-height: 26px;
    padding: 22px 0 0 28px; font-style: normal;
  }
  .insurance-note {
    position: absolute; left: 640px; top: 676px; width: 530px; height: 144px;
    background: var(--panel-grey);
    font-weight: 600; font-size: 17.5px; line-height: 27px; color: var(--ink);
    padding: 20px 18px 0 26px;
  }
</style>
</head>
<body>
<main class="flyer">
  <div class="hero-photo" role="img" aria-label="Photo of a white two-storey house standing in flood water"></div>
  <div class="blue-band"></div>

  <h1 class="title"><span class="storm">Storm</span><span class="restoration">Restoration</span></h1>

  <div class="brand">
    <span class="brand-dot"></span>
    <span class="brand-name">Brellwick Building Partners</span>
  </div>

  <p class="intro">We provide disaster relief to homeowners and or commercial property owners after a flood.</p>

  <div class="inset inset-fan"><div class="fill" role="img" aria-label="Photo of a blue drying fan on a wet floor"></div></div>
  <div class="inset inset-policy"><div class="fill" role="img" aria-label="Photo of a property insurance policy document"></div></div>

  <section class="service">
    <h2>Cleanup and Remediation</h2>
    <p>To start we offer cleanup and remediation which is taking out and disposing of all wet items in a home or business and the cutting out of walls, flooring and other items affected by a flood. We then provide remediation which includes the drying out of a home or business along with a dehumidifier to take all the moisture out of the air and to put it simply dry out the home. We also uses chemicals to clean and provide mold remediation to prevent to growth of mold.</p>
  </section>

  <div class="footer-strip"></div>
  <address class="contact">
    Brellwick Building Partners<br>
    48-10 Harlow Ave. Dunmore, NY 11482<br>
    Phone: 555-204-7730, Fax: 555-204-7731<br>
    Website: brellwickbuilding.com
  </address>
  <p class="insurance-note">We work directly with a customers insurance company if they have flood insurance and after that we provide the services to rebuild and bring their property back to its condition before the storm.</p>
</main>
</body>
</html>
```